Defense Attorney Business Card Design Project/ Stationary

I am looking for a distinctive business card design for my solo law practice.
I practice criminal defense, both juvenile and adult, including DUI. I am a very experienced attorney with prior military experience. The design should convey a traditional, old school flair, but not be too stodgy or uptight. Some color. My logo should appear.

Project Deadline Extended Reason: I misunderstood how this project works and I was not prepared with my logo when this project ran the first time. Added Thursday, November 13, 2014

Reason: I was sent overseas on military duty last year, which interrupted this project. Thank you for your participation... I hope we can get this done this week! Thank you, Des

Target Market(s)

Regular everyday people looking for strong, knowledgeable, authoritative representation while they are faced with criminal charges. Many have never been charged with a crime before. A reassuring air is therefore desired.

Industry/Entity Type

Business

Contact Information for Business Card

My information is:
Desmond R. Whitcombe, Attorney at Law
735 Linden Avenue Suite 300
Oakland, California 94618
Tel: (510) 555-0183
Fax: (510) 555-0162
email: deswhitcombelaw@mailbrook.net
web: www.deswhitcombelaw.net

Font styles to use
Serif
Sans Serif
Decorative

Colors
0255a3
ffffff

Requirements
Must have
• Sharp lines, bold elements. Conservative use of colors, such as deep blues, burgundy, grays for example.
• While my logo says "Des Whitcombe", it should be modified to show "Desmond R. Whitcombe".
Should not have
• Cliche imagery such as scales of justice, gavels, Tower of Varenholt, etc.

```html
<!DOCTYPE html>
<html lang="en">
<head>
<meta charset="utf-8">
<title>Desmond R. Whitcombe — Business Card</title>
<link href="https://fonts.googleapis.com/css2?family=Oswald:wght@500&family=Open+Sans:wght@400;600&display=swap" rel="stylesheet">
<style>
  :root {
    --navy: #124a63;
    --frame-grey: #d9dadc;
    --band-grey: #a7aaae;
    --paper: #ffffff;
    --ink: #3a3d42;
    --ink-soft: #6b6f75;
    --backdrop: #ecebe8;
  }
  * { box-sizing: border-box; margin: 0; padding: 0; }
  html, body {
    width: 1057px; height: 1200px; overflow: hidden;
    background: var(--backdrop);
  }
  .sheet {
    width: 1057px; height: 1200px;
    display: flex; justify-content: center; align-items: center; gap: 60px;
  }
  .card {
    width: 440px; height: 770px;
    box-shadow: 0 6px 18px rgba(0,0,0,0.12);
    position: relative;
  }

  /* Front */
  .card--front { background: var(--frame-grey); padding: 18px; }
  .card-front__inner {
    width: 100%; height: 100%;
    background: var(--paper);
    display: flex; flex-direction: column;
  }
  .brand {
    height: 250px;
    display: flex; justify-content: center; align-items: center; gap: 12px;
  }
  .brand__mark {
    width: 14px; height: 14px; background: var(--navy); border-radius: 50%; flex: none;
  }
  .brand__name {
    font-family: "Open Sans", sans-serif; font-weight: 600;
    font-size: 30px; color: var(--navy);
  }
  .person { padding: 30px 0 0 34px; height: 130px; }
  .person__name {
    font-family: "Oswald", sans-serif; font-weight: 500;
    font-size: 30px; letter-spacing: 1px; color: var(--ink);
    text-transform: uppercase; line-height: 1.1;
  }
  .person__title {
    font-family: "Open Sans", sans-serif; font-weight: 600;
    font-size: 12px; letter-spacing: 1.5px; color: var(--ink-soft);
    text-transform: uppercase; margin-top: 6px;
  }
  .contacts {
    background: var(--navy);
    height: 226px;
    padding: 28px 34px;
    display: flex; flex-direction: column; justify-content: space-between;
    list-style: none;
  }
  .contact {
    display: flex; align-items: center; gap: 16px;
    font-family: "Open Sans", sans-serif; font-size: 14px; color: #ffffff;
    letter-spacing: 0.3px;
  }
  .contact__icon {
    width: 28px; height: 28px; border-radius: 5px; background: #ffffff;
    display: flex; align-items: center; justify-content: center; flex: none;
  }
  .contact__icon svg { width: 17px; height: 17px; }
  .address {
    background: var(--band-grey);
    height: 78px;
    padding: 0 34px;
    display: flex; align-items: center; gap: 16px;
    font-family: "Open Sans", sans-serif; font-size: 13px; line-height: 1.45; color: #ffffff;
  }
  .address .contact__icon { width: 26px; height: 26px; }

  /* Back */
  .card--back { background: var(--navy); padding: 30px; }
  .card-back__inner {
    width: 100%; height: 100%;
    background: linear-gradient(160deg, #ffffff 0%, #f1f2f3 100%);
    display: flex; align-items: center; justify-content: center; gap: 14px;
  }
  .card-back__inner .brand__mark { width: 18px; height: 18px; }
  .card-back__inner .brand__name { font-size: 34px; }
</style>
</head>
<body>
<main class="sheet">

  <section class="card card--front" aria-label="Business card front">
    <div class="card-front__inner">
      <header class="brand">
        <span class="brand__mark"></span>
        <span class="brand__name">Des Whitcombe</span>
      </header>

      <div class="person">
        <p class="person__name">Desmond R. Whitcombe</p>
        <p class="person__title">Attorney at Law</p>
      </div>

      <ul class="contacts">
        <li class="contact">
          <span class="contact__icon">
            <svg viewBox="0 0 24 24"><path fill="#124a63" d="M6.6 10.8a15 15 0 0 0 6.6 6.6l2.2-2.2a1 1 0 0 1 1-.25 11.4 11.4 0 0 0 3.6.57 1 1 0 0 1 1 1V20a1 1 0 0 1-1 1A17 17 0 0 1 3 4a1 1 0 0 1 1-1h3.5a1 1 0 0 1 1 1c0 1.25.2 2.45.57 3.6a1 1 0 0 1-.25 1z"/></svg>
          </span>
          (510) 555-0183
        </li>
        <li class="contact">
          <span class="contact__icon">
            <svg viewBox="0 0 24 24"><path fill="#124a63" d="M6 3h12v5H6zM4 9h16a2 2 0 0 1 2 2v6h-4v4H6v-4H2v-6a2 2 0 0 1 2-2zm4 7v3h8v-3z"/></svg>
          </span>
          (510) 555-0162
        </li>
        <li class="contact">
          <span class="contact__icon">
            <svg viewBox="0 0 24 24"><path fill="#124a63" d="M3 5h18a1 1 0 0 1 1 1v12a1 1 0 0 1-1 1H3a1 1 0 0 1-1-1V6a1 1 0 0 1 1-1zm1 2.2V17h16V7.2l-8 5.3z"/></svg>
          </span>
          deswhitcombelaw@mailbrook.net
        </li>
        <li class="contact">
          <span class="contact__icon">
            <svg viewBox="0 0 24 24"><circle cx="12" cy="12" r="9" fill="none" stroke="#124a63" stroke-width="2"/><path d="M3 12h18M12 3c3 3 3 15 0 18M12 3c-3 3-3 15 0 18" fill="none" stroke="#124a63" stroke-width="1.6"/></svg>
          </span>
          www.deswhitcombelaw.net
        </li>
      </ul>

      <div class="address">
        <span class="contact__icon">
          <svg viewBox="0 0 24 24"><path fill="#a7aaae" d="M12 2a7 7 0 0 0-7 7c0 5 7 13 7 13s7-8 7-13a7 7 0 0 0-7-7zm0 9.5A2.5 2.5 0 1 1 12 6.5a2.5 2.5 0 0 1 0 5z"/></svg>
        </span>
        <address style="font-style: normal;">735 Linden Avenue Suite 300<br>Oakland, California 94618</address>
      </div>
    </div>
  </section>

  <section class="card card--back" aria-label="Business card back">
    <div class="card-back__inner">
      <span class="brand__mark"></span>
      <span class="brand__name">Des Whitcombe</span>
    </div>
  </section>

</main>
</body>
</html>
```